Telecommunications/Power civil contractor needs business card design

Were a new telecommunications/power underground civil contractor that is looking for a new business card design. Our company colours are silver or grey and orange. Feel free to use the white background logo or the black background logo.

Target Market(s)

Local contractors, utility companies, private sector mining/energy companies, developers.

Industry/Entity Type

Telecommunications

Contact Information for Business Card

Each card will need the following info:
Persons name:
Title:
E-mail:
Phone number:
Shop Address:
Mailing Address:

Requirements
Must have
• Each card will need the following info:
• Persons name:
• Title:
• E-mail:
• Phone number:
• Shop Address:
• Mailing Address:

```html
<!DOCTYPE html>
<html lang="en">
<head>
<meta charset="utf-8">
<title>Tamarack Contracting Inc – Business Card</title>
<link rel="stylesheet" href="https://fonts.googleapis.com/css2?family=Questrial&display=swap">
<style>
  :root {
    --bg: #2a2826;
    --card-dark: #2b2b2c;
    --card-light: #f2f2f2;
    --orange: #e2552a;
    --silver: #c9c9c9;
    --text-light: #ececec;
    --rule: #5a5a5a;
  }
  * { margin: 0; padding: 0; box-sizing: border-box; }
  html, body { width: 1200px; height: 727px; overflow: hidden; }
  body {
    background: var(--bg);
    font-family: "Questrial", sans-serif;
    position: relative;
  }
  .card {
    position: absolute;
    top: 209px;
    width: 540px;
    height: 309px;
    overflow: hidden;
    box-shadow: 0 10px 30px rgba(0,0,0,.45);
  }
  .card--front { left: 50px; background: var(--card-dark); }
  .card--back { left: 610px; background: var(--card-dark); }

  .front__brand-panel {
    position: absolute; left: 0; top: 0;
    width: 200px; height: 100%;
    background: var(--card-light);
    display: flex; flex-direction: column;
    align-items: center; justify-content: center;
    gap: 10px;
  }
  .brand-dot {
    width: 40px; height: 40px; border-radius: 50%;
    background: var(--orange);
  }
  .brand-name {
    color: var(--orange);
    font-size: 17px;
    letter-spacing: 1px;
    text-transform: uppercase;
    text-align: center;
    line-height: 1.25;
  }
  .front__accent-strip {
    position: absolute; left: 200px; top: 0;
    width: 44px; height: 100%;
    background: var(--orange);
  }
  .contact-icons {
    position: absolute; left: 207px; top: 108px;
    display: flex; flex-direction: column; gap: 16px;
  }
  .contact-icon {
    width: 30px; height: 30px; border-radius: 50%;
    background: #f4f4f4;
    display: flex; align-items: center; justify-content: center;
  }
  .front__details {
    position: absolute; left: 272px; top: 58px; right: 30px;
    color: var(--text-light);
  }
  .person-name { font-size: 22px; }
  .person-title { font-size: 13px; color: var(--orange); margin-top: 2px; }
  .detail-line {
    font-size: 14px;
    padding: 12px 0 8px;
    border-bottom: 1px solid var(--rule);
  }
  .detail-line:first-of-type { margin-top: 10px; }
  .address { font-size: 13px; line-height: 1.6; padding-top: 10px; }

  .back__wave { position: absolute; inset: 0; }
  .back__brand {
    position: absolute; right: 40px; top: 120px;
    display: flex; align-items: center; gap: 14px;
  }
  .back__brand .brand-dot { width: 48px; height: 48px; }
  .back__brand .brand-name { font-size: 22px; text-align: left; }
</style>
</head>
<body>
  <section class="card card--front">
    <div class="front__brand-panel">
      <div class="brand-dot"></div>
      <div class="brand-name">Tamarack<br>Contracting Inc</div>
    </div>
    <div class="front__accent-strip"></div>
    <div class="contact-icons">
      <div class="contact-icon">
        <svg width="16" height="16" viewBox="0 0 16 16"><path d="M3 2h3l1 3-2 1c1 2 2 3 4 4l1-2 3 1v3c0 1-1 2-2 2C6 14 2 10 2 4c0-1 0-2 1-2z" fill="#e2552a"/></svg>
      </div>
      <div class="contact-icon">
        <svg width="16" height="16" viewBox="0 0 16 16"><rect x="2" y="4" width="12" height="8" fill="#e2552a"/><path d="M2 4l6 5 6-5" fill="none" stroke="#f4f4f4" stroke-width="1.2"/></svg>
      </div>
      <div class="contact-icon">
        <svg width="16" height="16" viewBox="0 0 16 16"><path d="M8 1a5 5 0 0 1 5 5c0 4-5 9-5 9S3 10 3 6a5 5 0 0 1 5-5z" fill="#e2552a"/><circle cx="8" cy="6" r="2" fill="#f4f4f4"/></svg>
      </div>
    </div>
    <div class="front__details">
      <div class="person-name">Your Name</div>
      <div class="person-title">Job Title</div>
      <div class="detail-line">000 000 0000</div>
      <div class="detail-line">email@example.com</div>
      <div class="address">Shop-00, St. Name, City, ST-0000<br>00, St. Name, City, ST-0000</div>
    </div>
  </section>

  <section class="card card--back">
    <svg class="back__wave" viewBox="0 0 540 309" preserveAspectRatio="none">
      <path d="M0 0 H150 C200 60 230 160 300 210 C380 265 460 270 540 272 V309 H0 Z" fill="#232324"/>
      <path d="M150 0 C200 60 230 160 300 210 C380 265 460 270 540 272" fill="none" stroke="#e2552a" stroke-width="5"/>
    </svg>
    <div class="back__brand">
      <div class="brand-dot"></div>
      <div class="brand-name">Tamarack<br>Contracting Inc</div>
    </div>
  </section>
</body>
</html>
```